VELMOR Website Design

We need a website designed for our company VELMOR. We are a luxury lifestyle club that will provide benefits and services for our members. The site should be clean & sleek, preferably using black and white (or darker colors). (example sites: brastelle.com, fovix.com)

Here is a link of a sample page I did using wix. (https://dunmerel7.pagebuildr.com/mysite) This can be used to get a general idea.

Target Market(s)

Upper Middle Class in the United States

Number of Pages Required

5+ page

Font styles to use
Sans Serif
Other font styles liked:
• Arial (or other similar fonts)

Requirements
Must have
• A clean design that is eye-catching and speaks to our company.
Nice to have
• Ideas for copy.

```html
<!DOCTYPE html>
<html lang="en">
<head>
<meta charset="utf-8">
<title>VELMOR — A Members Only Lifestyle Club</title>
<link rel="stylesheet" href="https://fonts.googleapis.com/css2?family=Montserrat:wght@300;400;500;600&family=Nunito+Sans:wght@300;400;600;700&display=swap">
<style>
:root{
  --bronze:#6e563f;
  --bronze-line:#8a6a4c;
  --ink:#1b1b1b;
  --text:#2c2c2c;
  --muted:#8c8c8c;
  --white:#ffffff;
  --night:#15171b;
  --footer:#050505;
  --star:#b08a5b;
  --head:"Montserrat", sans-serif;
  --body:"Nunito Sans", sans-serif;
}
*{box-sizing:border-box;margin:0;padding:0}
html,body{width:1200px;height:3056px;overflow:hidden}
body{position:relative;background:var(--white);font-family:var(--body);color:var(--text)}
a{text-decoration:none}
.abs{position:absolute}
section,header,footer{position:absolute;left:0;width:1200px;overflow:hidden}
.h2{position:absolute;left:0;width:1200px;text-align:center;font-family:var(--head);font-weight:400;font-size:30px;letter-spacing:.5px;text-transform:uppercase;white-space:nowrap}
.rule{position:absolute;left:574px;width:52px;height:2px;background:var(--bronze-line)}
.btn{position:absolute;display:flex;align-items:center;justify-content:center;font-family:var(--head);font-size:11px;letter-spacing:.6px;text-transform:uppercase;color:var(--white)}
.btn.solid{background:var(--bronze)}
.btn.ghost{border:1px solid rgba(255,255,255,.7)}
.photo{position:absolute}

/* hero */
.hero{top:0;height:534px}
.hero .photo{inset:0;background:linear-gradient(115deg,#5d5a58 0%,#a48f7e 25%,#6e6d70 50%,#c2b2a3 75%,#55524f 100%)}
.hero .shade{position:absolute;inset:0;background:rgba(20,18,16,.35)}
.logo{font-family:var(--head);font-weight:400;font-size:27px;letter-spacing:1.5px;color:var(--white)}
.nav{position:absolute;top:24px;font-family:var(--head);font-size:11px;color:var(--white);text-transform:uppercase}
.nav span{position:absolute;white-space:nowrap}
.hero-frame{position:absolute;left:305px;top:240px;width:587px;height:104px;border:1px solid rgba(255,255,255,.75)}
.hero-title{left:0;top:226px;width:1200px;text-align:center;color:var(--white);font-family:var(--head);font-size:29px;letter-spacing:.5px}
.hero-sub{left:0;width:1200px;text-align:center;top:280px;font-size:14px;color:var(--white)}

/* welcome */
.welcome{top:534px;height:266px;text-align:center}
.welcome p{position:absolute;left:280px;top:114px;width:640px;font-size:11px;line-height:24px;color:#555}

/* services */
.services{top:800px;height:394px;background:var(--night)}
.services .photo{inset:0;background:linear-gradient(90deg,#2a2622,#3b3430 40%,#2e2927 70%,#1f1d1c);opacity:.9}
.services .shade{position:absolute;inset:0;background:rgba(10,10,12,.55)}
.card{position:absolute;top:168px;height:160px}
.card .img{position:absolute;inset:0}
.card .label{position:absolute;left:0;right:0;bottom:0;height:32px;background:rgba(0,0,0,.7);color:var(--white);font-family:var(--head);font-size:12px;display:flex;align-items:center;justify-content:center;text-transform:uppercase;white-space:nowrap}
.card.featured{top:160px;height:178px;border:3px solid var(--white)}
.card.featured .label{background:var(--bronze);left:8px;right:8px;bottom:8px}
.arrow-dot{position:absolute;width:26px;height:26px;border-radius:50%;background:#8a6a4c;border:2px solid #c9b49a}

/* video */
.video{top:1194px;height:436px}
.video .title{font-family:var(--head);font-weight:400;font-size:31px;color:var(--ink);position:absolute;left:690px;width:370px;text-align:center;top:136px;white-space:nowrap}
.video p{position:absolute;left:690px;width:370px;text-align:center;font-size:12px;line-height:27px;color:var(--ink);top:190px}

/* split */
.split{top:1630px;height:336px;background:var(--night)}
.split .half{position:absolute;top:0;height:336px;width:599px}
.split .shade{position:absolute;inset:0;background:rgba(0,0,0,.5)}
.split h3{position:absolute;top:48px;font-family:var(--head);font-weight:400;font-size:30px;color:var(--white);text-transform:uppercase;white-space:nowrap}
.split p{position:absolute;top:108px;width:430px;font-size:11.5px;line-height:27px;color:var(--white)}

/* events */
.events{top:1966px;height:393px}
.event-img{position:absolute;top:118px;width:240px;height:161px}
.event-text{position:absolute;top:126px;width:205px}
.event-date{font-size:10px;color:#555}
.event-title{font-family:var(--body);font-weight:700;font-size:13.5px;line-height:20px;color:var(--ink);margin-top:10px}
.event-body{font-size:10.5px;line-height:18px;color:var(--muted);margin-top:12px}

/* reviews */
.reviews{top:2359px;height:334px;background:var(--night)}
.reviews .photo{inset:0;background:linear-gradient(180deg,#33302e,#1f2024 55%,#121417)}
.reviews .shade{position:absolute;inset:0;background:rgba(0,0,0,.35)}
.review{position:absolute;top:118px;width:350px;height:134px;background:var(--white)}
.review .avatar{position:absolute;left:6px;top:30px;width:76px;height:76px;background:linear-gradient(180deg,#c9c3bd,#8a8581)}
.review .quote{position:absolute;left:104px;top:14px;width:228px;font-size:10.5px;line-height:17px;color:#666}
.review .name{position:absolute;left:104px;bottom:14px;font-family:var(--head);font-size:11.5px;font-weight:500;color:var(--ink);text-transform:uppercase;display:flex;gap:12px;align-items:center;white-space:nowrap}
.review .stars{color:var(--star);font-size:10px;letter-spacing:1px}
.review .line{position:absolute;left:84px;right:14px;bottom:40px;height:1px;background:#ddd}
.rev-arrows{position:absolute;left:100px;top:130px;width:60px;height:110px}

/* newsletter */
.newsletter{top:2693px;height:226px;text-align:center}
.newsletter p{position:absolute;left:0;width:1200px;top:96px;font-size:12px;color:#777}
.field{position:absolute;left:350px;top:134px;width:460px;height:40px;background:#ececec;font-size:11px;font-style:italic;color:#888;display:flex;align-items:center;padding-left:18px}
.send{position:absolute;left:810px;top:134px;width:40px;height:40px;background:var(--bronze);display:flex;align-items:center;justify-content:center}

/* footer */
.footer{top:2919px;height:137px;background:var(--footer);color:var(--white)}
.contact{position:absolute;top:60px;font-size:10px;display:flex;align-items:center;gap:10px;white-space:nowrap}
.contact .ico{width:26px;height:26px;border:1px solid #777;display:flex;align-items:center;justify-content:center}
.social{position:absolute;left:222px;top:66px;display:flex;gap:8px}
.social i{width:8px;height:8px;border-radius:50%;background:var(--white);display:block}
.foot-rule{position:absolute;left:0;right:0;top:101px;height:1px;background:#333}
.legal{position:absolute;top:115px;font-size:9.5px;text-transform:uppercase;letter-spacing:.3px;white-space:nowrap}
</style>
</head>
<body>

<header class="hero">
  <div class="photo" role="img" aria-label="Photo of friends toasting on a yacht at sea"></div>
  <div class="shade"></div>
  <div class="logo abs" style="left:108px;top:14px">VELMOR</div>
  <nav class="nav" style="left:0">
    <span style="left:455px">Home</span>
    <span style="left:546px">About Us</span>
    <span style="left:660px">Services &amp; Benefits</span>
    <span style="left:831px">Events</span>
    <span style="left:930px">Apply</span>
    <span style="left:1020px">Contact Us</span>
  </nav>
  <div class="hero-frame"></div>
  <div class="abs" style="left:340px;top:226px;width:520px;height:36px;background:rgba(95,88,82,.6)"></div>
  <div class="hero-title abs">A MEMBERS ONLY LIFESTYLE CLUB</div>
  <div class="hero-sub abs">VELMOR membership provides you with amazing benefits and services.</div>
  <a class="btn ghost" style="left:433px;top:326px;width:159px;height:38px">Join The Club</a>
  <a class="btn ghost" style="left:607px;top:326px;width:158px;height:38px">Member Login</a>
  <svg class="abs" style="left:590px;top:486px" width="20" height="32" viewBox="0 0 20 32"><rect x="1" y="1" width="18" height="30" rx="9" fill="none" stroke="#fff" stroke-width="1.5"/><line x1="10" y1="8" x2="10" y2="16" stroke="#fff" stroke-width="2"/></svg>
</header>

<section class="welcome">
  <h2 class="h2" style="top:46px;color:var(--ink)">Welcome to VELMOR</h2>
  <div class="rule" style="top:88px"></div>
  <p>VELMOR is a members only lifestyle club founded in order to bring the best services, experiences, and opportunities to our diverse community of members. Our members consist of creatives, athletes, artists, and other professionals.</p>
  <a class="btn solid" style="left:545px;top:178px;width:121px;height:35px">Learn More</a>
</section>

<section class="services">
  <div class="photo" role="img" aria-label="Crowd celebrating at a night party"></div>
  <div class="shade"></div>
  <h2 class="h2" style="top:46px;color:var(--white)">Services &amp; Benefits</h2>
  <div class="rule" style="top:88px"></div>
  <div class="abs" style="left:0;width:1200px;top:116px;text-align:center;font-size:11px;color:#ddd">VELMOR membership provides you with amazing benefits and services.</div>

  <div class="card" style="left:120px;width:105px"><div class="img" role="img" aria-label="Photo of a business handshake" style="background:linear-gradient(135deg,#c8c4c0,#6a655f)"></div><div class="label">Services</div></div>
  <div class="card" style="left:240px;width:228px"><div class="img" role="img" aria-label="Photo of a financial chart on a screen" style="background:linear-gradient(135deg,#2f4f7a,#0f1c33 60%,#6c7f99)"></div><div class="label">Investment Services</div></div>
  <div class="card featured" style="left:483px;width:234px"><div class="img" role="img" aria-label="Photo of a concert crowd under purple lights" style="background:linear-gradient(160deg,#e05ac7,#7a2a9a 45%,#2a0f3a)"></div><div class="label">Investment Services</div></div>
  <div class="card" style="left:733px;width:228px"><div class="img" role="img" aria-label="Photo of travellers beside a private jet" style="background:linear-gradient(180deg,#9fb8d6,#e6e8ea 55%,#8b8f94)"></div><div class="label">Private Jet Travel</div></div>
  <div class="card" style="left:973px;width:107px"><div class="img" role="img" aria-label="Photo of a lawyer signing papers" style="background:linear-gradient(135deg,#d9d2c8,#7b6a58)"></div><div class="label">Lawyer</div></div>

  <div class="arrow-dot" style="left:97px;top:236px"></div>
  <svg class="abs" style="left:104px;top:243px" width="12" height="12" viewBox="0 0 12 12"><path d="M8 2 L4 6 L8 10" fill="none" stroke="#fff" stroke-width="1.6"/></svg>
  <div class="arrow-dot" style="left:1077px;top:236px"></div>
  <svg class="abs" style="left:1084px;top:243px" width="12" height="12" viewBox="0 0 12 12"><path d="M4 2 L8 6 L4 10" fill="none" stroke="#fff" stroke-width="1.6"/></svg>
  <div class="abs" style="left:596px;top:340px;width:7px;height:7px;border-radius:50%;background:#fff"></div>
</section>

<section class="video">
  <div class="photo" role="img" aria-label="Photo of a private jet flying above clouds" style="left:110px;top:52px;width:533px;height:332px;background:linear-gradient(180deg,#3d4a5c,#7a8696 45%,#c7b8a6 60%,#4d5866)"></div>
  <svg class="abs" style="left:352px;top:192px" width="50" height="50" viewBox="0 0 50 50"><circle cx="25" cy="25" r="23" fill="rgba(0,0,0,.55)" stroke="#fff" stroke-width="2"/><path d="M20 15 L34 25 L20 35 Z" fill="#fff"/></svg>
  <h2 class="title">WATCH OUR VIDEO</h2>
  <p>Learn more about our club by watching this quick video.<br>we're sure you will love it!</p>
  <a class="btn solid" style="left:808px;top:256px;width:134px;height:32px">Apply Now</a>
</section>

<section class="split">
  <div class="half" style="left:0">
    <div class="photo" role="img" aria-label="Photo of a crowd at an outdoor festival" style="inset:0;background:linear-gradient(160deg,#6c6a66,#3b3a38 50%,#1e1e1e)"></div>
    <div class="shade"></div>
    <h3 style="left:108px">Experiences</h3>
    <p style="left:108px">VELMOR organizes and supports a ton of private events and parties for our members. Members are also provided access to exclusive venues and events from our partners. Network with other members to build lasting relationships.</p>
    <a class="btn ghost" style="left:108px;top:250px;width:120px;height:34px">Learn More</a>
  </div>
  <div class="half" style="left:602px">
    <div class="photo" role="img" aria-label="Photo of long-tail boats on a tropical beach" style="inset:0;background:linear-gradient(180deg,#3f6f88,#2c5668 45%,#6a5a45 80%,#3a3226)"></div>
    <div class="shade"></div>
    <h3 style="right:110px">We Are VELMOR</h3>
    <p style="right:110px;text-align:right">Built in the image of a "Multi-Family Office", VELMOR provides members with access to just about any service, experience, and event desirable.<br>VELMOR is truly the most exclusive lifestyle club out there.</p>
    <a class="btn ghost" style="right:110px;top:250px;width:120px;height:34px">Apply Now</a>
  </div>
</section>

<section class="events">
  <h2 class="h2" style="top:44px;color:var(--ink)">Events</h2>
  <div class="rule" style="top:86px"></div>
  <div class="event-img" role="img" aria-label="Photo of a DJ performing under colourful lights" style="left:110px;background:linear-gradient(135deg,#2f8fd6,#e9c92c 45%,#d0407a 75%,#2a1e4a)"></div>
  <div class="event-text" style="left:370px">
    <div class="event-date">4th october 2018</div>
    <div class="event-title">Lorem ipsum dolor sit consectetur adipiscing elit.</div>
    <div class="event-body">Suspendisse at nunc ut libero gravida fringilla. Vestibulum pretium luctus tincidunt. Fusce justo magna, ornare eu mauris eleifend congue felis... [+]</div>
  </div>
  <div class="abs" style="left:600px;top:118px;width:1px;height:161px;background:#e2e2e2"></div>
  <div class="event-img" role="img" aria-label="Photo of spinning fire sparks at night" style="left:625px;background:radial-gradient(circle at 50% 50%,#f7b44a,#b8531a 40%,#2a150c 80%)"></div>
  <div class="event-text" style="left:885px">
    <div class="event-date">10th october 2018</div>
    <div class="event-title">Lorem ipsum dolor sit consectetur adipiscing elit.</div>
    <div class="event-body">Suspendisse at nunc ut libero gravida fringilla. Vestibulum pretium luctus tincidunt. Fusce justo magna, ornare eu mauris eleifend congue felis... [+]</div>
  </div>
  <a class="btn solid" style="left:517px;top:306px;width:160px;height:34px">View All Events</a>
</section>

<section class="reviews">
  <div class="photo" role="img" aria-label="Photo of a luxury villa with pool at dusk"></div>
  <div class="shade"></div>
  <h2 class="h2" style="top:44px;color:var(--white)">Members Reviews</h2>
  <div class="rule" style="top:86px"></div>
  <svg class="rev-arrows" viewBox="0 0 60 110"><path d="M30 2 L58 30 L58 80 L30 108 L2 80 L2 30 Z" fill="#8a6a4c" opacity=".85"/><circle cx="30" cy="34" r="20" fill="none" stroke="#fff" stroke-width="2"/><path d="M22 34 H38 M32 28 L38 34 L32 40" fill="none" stroke="#fff" stroke-width="2"/><circle cx="30" cy="78" r="20" fill="none" stroke="#fff" stroke-width="2"/><path d="M38 78 H22 M28 72 L22 78 L28 84" fill="none" stroke="#fff" stroke-width="2"/></svg>

  <div class="review" style="left:235px">
    <div class="avatar" role="img" aria-label="Portrait photo of a member"></div>
    <div class="quote">Suspendisse at nunc ut libero gravida fringilla. Vestibulum pretium luctus tincidunt. Fusce justo magna, ornare eu mauris eleifend congue felis.</div>
    <div class="line"></div>
    <div class="name">Marco Delane <span class="stars">★★★★★</span></div>
  </div>
  <div class="review" style="left:610px">
    <div class="avatar" role="img" aria-label="Portrait photo of a member"></div>
    <div class="quote">Suspendisse at nunc ut libero gravida fringilla. Vestibulum pretium luctus tincidunt. Fusce justo magna, ornare eu mauris eleifend congue felis.</div>
    <div class="line"></div>
    <div class="name">Lena Harrow <span class="stars">★★★★★</span></div>
  </div>
  <div class="review" style="left:980px">
    <div class="avatar" role="img" aria-label="Portrait photo of a member"></div>
    <div class="quote">Suspendisse at nunc ut libero gravida fringilla. Vestibulum pretium luctus tincidunt. Fusce justo magna, ornare eu mauris eleifend congue felis.</div>
    <div class="line"></div>
    <div class="name">Owen Trask <span class="stars">★★★★★</span></div>
  </div>
</section>

<section class="newsletter">
  <h2 class="h2" style="top:42px;color:var(--ink)">Subscribe to our Newsletter</h2>
  <div class="rule" style="top:82px"></div>
  <p>Subscribe to our newsletter to receive all the latest VELMOR news and updates to your inbox.</p>
  <div class="field">Enter Your Email Address...</div>
  <div class="send"><svg width="16" height="16" viewBox="0 0 16 16"><path d="M1 8 L15 1 L11 15 L8 9 Z" fill="#fff"/></svg></div>
</section>

<footer class="footer">
  <div class="logo abs" style="left:208px;top:20px;font-size:28px">VELMOR</div>
  <div class="social"><i></i><i></i><i></i><i></i><i></i></div>
  <nav class="nav" style="left:0">
    <span style="left:455px">Home</span>
    <span style="left:527px">About Us</span>
    <span style="left:620px">Services &amp; Benefits</span>
    <span style="left:772px">Events</span>
    <span style="left:850px">Apply</span>
    <span style="left:922px">Contact Us</span>
  </nav>
  <div class="contact" style="left:455px"><span class="ico"><svg width="10" height="13" viewBox="0 0 10 13"><path d="M5 12 C1 7 1 5 1 5 A4 4 0 0 1 9 5 C9 5 9 7 5 12 Z" fill="#fff"/><circle cx="5" cy="5" r="1.5" fill="#000"/></svg></span>VELMOR Lorem ipsum dolor sit vitae sit amet 488436</div>
  <div class="contact" style="left:755px"><span class="ico"><svg width="12" height="12" viewBox="0 0 12 12"><path d="M2 1 L4.5 1 L5.5 3.8 L4 5 C4.7 6.6 5.4 7.3 7 8 L8.2 6.5 L11 7.5 L11 10 C6 10.5 1.5 6 2 1 Z" fill="#fff"/></svg></span>555-214-7780</div>
  <div class="contact" style="left:885px"><span class="ico"><svg width="12" height="9" viewBox="0 0 12 9"><rect x="0.5" y="0.5" width="11" height="8" fill="#fff"/><path d="M0.5 0.5 L6 5 L11.5 0.5" fill="none" stroke="#000"/></svg></span>info@velmor.com</div>
  <div class="foot-rule"></div>
  <div class="legal" style="left:210px">© Copyright 2018 VELMOR. All rights reserved.</div>
  <div class="legal" style="left:988px">Privacy | Policy | FAQs</div>
</footer>

</body>
</html>
```